BrightPath Medical Exercise, LLC specializes in post rehab medical exercise for clients who have been discharged from physical therapy and/or other medical services and are in need of continued cardiovascular, strength, flexibility, endurance training and management of their medical conditions. We strive to bridge the gap between healthcare and fitness by staying in communication with the referring physician and /or physical therapist with updated progress notes to follow each clients progression, making sure each client is appropriate for exercise and identifying any red flags throughout the initial assessment and screening of the client, and referring those clients back to the physician and/or therapist when necessary.
Colors
Designer to choose colors to be used in the design.
Requirements
Must have
- Pictures of a trainer working with a client one on one during exercise, and group exercise
Nice to have
- Pictures that portray the bridge between healthcare and fitness
Should not have
- Cursive writing

```html
<!DOCTYPE html>
<html lang="en">
<head>
<meta charset="utf-8">
<title>BrightPath Medical Exercise, LLC – Conditions Rack Card</title>
<link rel="stylesheet" href="https://fonts.googleapis.com/css2?family=Montserrat:wght@400;500;700;800&display=swap">
<style>
  :root {
    --page-bg: #ececea;
    --card-bg: #f4f3f2;
    --brand-red: #e0262a;
    --ink: #1d1d1f;
    --ink-soft: #2e2e30;
    --photo-light-1: #f6f5f4;
    --photo-light-2: #e6e2df;
    --photo-light-3: #efeceb;
    --deck-dark: #1f2a25;
    --deck-mid: #4a4035;
    --deck-wood: #b39b82;
    --deck-wood-light: #d4c2ad;
  }
  * { box-sizing: border-box; margin: 0; padding: 0; }
  html, body {
    width: 1200px; height: 1080px; overflow: hidden;
    background: var(--page-bg);
    font-family: "Montserrat", Arial, sans-serif;
    color: var(--ink);
  }
  .rack-card {
    position: absolute; left: 355px; top: 20px;
    width: 490px; height: 1040px;
    background: var(--card-bg);
    overflow: hidden;
    box-shadow: 0 6px 24px rgba(0,0,0,.18);
  }
  .top-band { position: absolute; inset: 0 0 auto 0; height: 10px; background: var(--brand-red); z-index: 3; }
  .backdrop-photo {
    position: absolute; left: 0; top: 10px; width: 100%; height: 760px;
    background:
      radial-gradient(ellipse at 35% 38%, var(--photo-light-2) 0%, transparent 45%),
      radial-gradient(ellipse at 78% 55%, var(--photo-light-2) 0%, transparent 40%),
      linear-gradient(180deg, var(--photo-light-1), var(--photo-light-3));
    z-index: 1;
  }
  .content { position: relative; z-index: 2; padding: 38px 30px 0 30px; }
  .headline-intro {
    font-weight: 500; font-size: 20px; letter-spacing: .04em; text-transform: uppercase;
    color: var(--ink-soft); line-height: 1.1;
  }
  .headline-main {
    font-weight: 800; font-size: 21px; letter-spacing: .03em; text-transform: uppercase;
    color: var(--brand-red); line-height: 1.15; margin-top: 2px;
  }
  .conditions {
    display: grid; grid-template-columns: 1fr 1fr; column-gap: 14px;
    margin-top: 22px;
  }
  .condition-list { list-style: none; }
  .condition-list li {
    position: relative; padding-left: 20px;
    font-size: 13px; font-weight: 500; line-height: 1.12;
    margin-bottom: 7px; color: var(--ink-soft);
  }
  .condition-list li::before {
    content: ""; position: absolute; left: 0; top: 4px;
    width: 8px; height: 7px; background: var(--brand-red);
  }
  .quote-block { position: relative; margin-top: 18px; height: 190px; }
  .quote-rule { position: absolute; height: 2px; background: var(--brand-red); }
  .quote-rule.top { left: 90px; right: 10px; top: 0; }
  .quote-rule.upper-mid { left: 60px; right: 60px; top: 58px; }
  .quote-rule.lower-mid { left: 10px; right: 100px; top: 124px; }
  .quote-rule.bottom { left: 70px; right: 30px; top: 178px; }
  .quote-mark {
    position: absolute; width: 58px; height: 58px; border-radius: 50%;
    background: var(--brand-red); color: var(--ink);
    font-family: Georgia, "Times New Roman", serif; font-weight: 700;
    font-size: 62px; line-height: 80px; text-align: center;
  }
  .quote-mark.open { left: 10px; top: 30px; }
  .quote-mark.close { right: 10px; top: 96px; }
  .quote-text {
    position: absolute; left: 80px; right: 80px; top: 62px;
    text-align: center; font-weight: 800; font-size: 16px; line-height: 1.2; color: var(--ink);
  }
  .quote-author {
    position: absolute; left: 60px; right: 60px; top: 140px;
    text-align: center; font-weight: 500; font-size: 17px; color: var(--ink-soft);
  }
  .equipment-photo { position: absolute; left: 0; bottom: 0; width: 100%; height: 280px; z-index: 2; }
</style>
</head>
<body>
  <article class="rack-card">
    <div class="top-band"></div>
    <div class="backdrop-photo" role="img" aria-label="Faded photo of a woman exercising with a light hand weight"></div>

    <div class="content">
      <h1 class="headline">
        <span class="headline-intro">We offer management</span><br>
        <span class="headline-main">of the following conditions and more:</span>
      </h1>

      <section class="conditions">
        <ul class="condition-list">
          <li>Diabetes AC</li>
          <li>Hypertension</li>
          <li>ACL Rupture</li>
          <li>Ankle Fracture</li>
          <li>Bicipital Tendonitis</li>
          <li>Total Hip Replacement</li>
          <li>Total Knee Replacement</li>
          <li>Spinal Stenosis</li>
          <li>Multiple Sclerosis</li>
          <li>Shoulder Dislocation</li>
          <li>Scoliosis</li>
          <li>Osteoporosis</li>
          <li>Osteoarthritis</li>
          <li>Cervical disc herniation</li>
        </ul>
        <ul class="condition-list">
          <li>Joint Separation</li>
          <li>Fibromyalgia</li>
          <li>Spondylothesis</li>
          <li>Parkinson's Disease</li>
          <li>Tibial Plateau Fracture</li>
          <li>Tennis Elbow/Golfer's Elbow</li>
          <li>Carpal Tunnel Syndrome</li>
          <li>Total Shoulder Replacement</li>
          <li>Bicipital Tendonitis</li>
          <li>Patello-Femoral Syndrome</li>
          <li>Rotator Cuff Syndrome</li>
          <li>Cervical Strain</li>
          <li>Impingement Syndrome</li>
          <li>Laminectomy</li>
        </ul>
      </section>

      <blockquote class="quote-block">
        <div class="quote-rule top"></div>
        <div class="quote-rule upper-mid"></div>
        <div class="quote-rule lower-mid"></div>
        <div class="quote-rule bottom"></div>
        <span class="quote-mark open">&#8220;</span>
        <p class="quote-text">Exercise is the key to long-term management of most medical conditions</p>
        <p class="quote-author">~ Daniel R Whitford, PhD, PT</p>
        <span class="quote-mark close">&#8221;</span>
      </blockquote>
    </div>

    <svg class="equipment-photo" viewBox="0 0 490 280" preserveAspectRatio="none">
      <defs>
        <linearGradient id="deckGradient" x1="0" y1="0" x2="0" y2="1">
          <stop offset="0" stop-color="var(--deck-dark)"/>
          <stop offset="0.4" stop-color="var(--deck-mid)"/>
          <stop offset="0.7" stop-color="var(--deck-wood)"/>
          <stop offset="1" stop-color="var(--deck-wood-light)"/>
        </linearGradient>
      </defs>
      <path d="M0 120 Q245 -10 490 60 L490 280 L0 280 Z" fill="url(#deckGradient)" role="img" aria-label="Photo of blue dumbbells standing on a wooden deck"/>
      <path d="M0 120 Q245 -10 490 60" fill="none" stroke="var(--brand-red)" stroke-width="6"/>
    </svg>
  </article>
</body>
</html>
```